Quillo Design Prize - $10,000 tablet app design contest, Event App Category

Quillo is a marketplace for Velo App Templates (similar to PageLoom templates). We want you to design an app template for sale in our marketplace which targets Event Apps (Velo Apps that are created around music festivals, tradeshows, conferences or other events).

It’s up to you to create pages or features for the App Template that you think are appropriate. Creativity will be rewarded! Here are some example pages or features that you could create:

• A welcome page
• Event details – when and where?
• A location map
• A contact details page
• An event calendar (what’s on when?)
• Social media integration
• Video or animations

Your design should be Vibrant, Engaging and Contemporary. If you have an Velo, download Quillo Viewer and download template examples in the download tab.

Your entry must include:
• A brief description of your template
• preview images of all pages of your template

Attached to this project are free templates to help you get started with your design. We have included:
1. A free portfolio template for designers/photographers
2. Icons and artwork to use in your template
3. Blank pages template
4. Form template
5. Video ad template

If you are selected as a finalist you will be required to submit an .oproject file containing:
• Your InDesign source files
• Preview images of your template
• All creative / stock assets used in the template (animations, video etc.)
• A text file with instructions on how to update the template
• A metadata .txt file containing template details and your information

How to enter:
1. Register at Marketplace and view the instructions under the welcome message https://marketplace.quillohub-example.com/welcome
2. Download Quillo Editor: https://support.quillohub-example.com/entries/58174096-quillo-editor
3. Use the free templates provided in this brief to create your designs and submit to Pencilyard

Reason: Due to the Christmas break we are extending the deadline of our competition. Thank you for time and effort - I will be providing feedback over the next couple of days! Best wishes, Loretta

Hi All,

I have received many screenshots with some great designs! I just wanted to clarify that you are designing Quillo app templates including Quillo features and not just page designs?

Read Tips for First Time Quilloers to guide you through the template creation process

Before you start designing templates for Quillo Marketplace

·       Read the Quality Standards

·       Read the Copyright Information 

·       Use the Template Quality Checklist to ensure your template follows our guidelines. 

What should my project file contain?

·       A folder containing your source files, e.g. InDesign. This must be named Source.

·       The Quillo content files. This must be named Bundle.

·       Instructions, explaining to a customer how to use your template.

Best wishes,

Loretta

Reason: We are extending the competition by 7 days to give you more time!

Reason: Hello - we have received 3 entries for this contest so we are extending the deadline by 7 days. Best wishes, Loretta :)

Target Market(s)

Entrepreneurs who wish to create Velo Apps by using our App design templates.

Industry/Entity Type

Events

Requirements
Must have
• You will need Quillo Editor to open the .oproject files attached to this brief. Get it here: https://support.quillohub-example.com/entries/58174096-quillo-editor
Should not have
• Low quality, fuzzy or blurry images
- Any stock images or content which you do not own the rights to
- Any material which could be considered inappropriate or offensive

```html
<!DOCTYPE html>
<html lang="en">
<head>
<meta charset="utf-8">
<title>Dance Party Fest – Welcome</title>
<link rel="stylesheet" href="https://fonts.googleapis.com/css2?family=Oswald:wght@500;600&family=Open+Sans:wght@400&display=swap">
<style>
  :root {
    --ink: #ffffff;
    --muted: #9a9a9a;
    --night: #000000;
    --magenta: #e0308f;
    --rose: #f06ab4;
    --crimson: #c21a3c;
    --violet: #7a2a8c;
    --band: rgba(20, 8, 20, 0.82);
  }
  html, body {
    margin: 0;
    padding: 0;
    width: 1200px;
    height: 900px;
    overflow: hidden;
    background: var(--night);
  }
  .welcome-screen {
    position: relative;
    width: 1200px;
    height: 900px;
    overflow: hidden;
    background: var(--night);
  }
  .party-backdrop {
    position: absolute;
    inset: 0;
    background:
      radial-gradient(ellipse 380px 300px at 1000px 320px, var(--rose) 0%, rgba(240,106,180,0) 70%),
      radial-gradient(ellipse 320px 280px at 140px 330px, var(--magenta) 0%, rgba(224,48,143,0) 75%),
      radial-gradient(ellipse 260px 200px at 880px 660px, rgba(255,140,60,0.7) 0%, rgba(255,140,60,0) 70%),
      linear-gradient(180deg, var(--crimson) 0%, var(--magenta) 30%, var(--violet) 50%, #3a0c2a 64%, var(--night) 74%, var(--night) 100%);
  }
  .center-band {
    position: absolute;
    top: 0;
    left: 363px;
    width: 469px;
    height: 900px;
    background: linear-gradient(180deg, var(--band) 0%, rgba(30,10,30,0.7) 50%, rgba(0,0,0,0.6) 75%, rgba(0,0,0,0) 100%);
  }
  .event-title {
    position: absolute;
    left: 0;
    right: 0;
    top: 296px;
    margin: 0;
    text-align: center;
    color: var(--ink);
    font-family: "Oswald", "Arial Narrow", sans-serif;
    text-transform: uppercase;
    line-height: 1;
  }
  .event-name {
    display: block;
    font-weight: 500;
    font-size: 58px;
    letter-spacing: -0.5px;
  }
  .event-date {
    display: block;
    margin-top: 4px;
    font-weight: 600;
    font-size: 108px;
    letter-spacing: -3px;
  }
  .next-button {
    position: absolute;
    left: 527px;
    top: 638px;
    width: 144px;
    height: 144px;
  }
  .swipe-hint {
    position: absolute;
    left: 0;
    right: 0;
    top: 812px;
    margin: 0;
    text-align: center;
    font-family: "Open Sans", Arial, sans-serif;
    font-size: 21px;
    color: var(--muted);
  }
  .swipe-hint strong {
    font-weight: 400;
    color: var(--ink);
  }
  .page-slider {
    position: absolute;
    left: 1047px;
    top: 815px;
    width: 153px;
    height: 24px;
  }
</style>
</head>
<body>
  <main class="welcome-screen">
    <div class="party-backdrop" role="img" aria-label="Pink and red dotted club lights with a silhouetted crowd dancing with raised arms"></div>
    <div class="center-band"></div>

    <h1 class="event-title">
      <span class="event-name">Dance Party Fest</span>
      <span class="event-date">01/14/2013</span>
    </h1>

    <svg class="next-button" viewBox="0 0 144 144" aria-label="Next page">
      <circle cx="72" cy="72" r="70" fill="none" stroke="#ffffff" stroke-width="3"/>
      <path d="M50 72 H92 M76 55 L93 72 L76 89" fill="none" stroke="#ffffff" stroke-width="4" stroke-linecap="round" stroke-linejoin="round"/>
    </svg>

    <p class="swipe-hint"><strong>swipe</strong> for more info</p>

    <svg class="page-slider" viewBox="0 0 153 24" aria-hidden="true">
      <line x1="19" y1="12" x2="153" y2="12" stroke="#ffffff" stroke-width="3"/>
      <circle cx="11" cy="12" r="8.5" fill="var(--night)" stroke="#ffffff" stroke-width="3"/>
    </svg>
  </main>
</body>
</html>
```